Web Design Project

We are re-starting this project.

This project is for a totally new look and design of a website for Wozzlent. www.wozzlent-example.com.

Wozzlent is a naming protocol for physical locations and can be used for fixed and mobile people, places and things. Find your friends, or find a business. Because Wozzlent locations point to precise geo-physical (GPS) co-ordinates, navigation to a location becomes totally reliable.
Updates

Please see the modified brief for this project

Target Market(s)

Every person and every business can have multiple !Wozzs (Wozzlent locations), so the website needs to be appealing and fun, but easy to use and functional

Industry/Entity Type

Business

Colors
34a6d7

Requirements
Must have
• Uniqueness!

```html
<!DOCTYPE html>
<html lang="en">
<head>
<meta charset="utf-8">
<title>Wozzlent</title>
<link href="https://fonts.googleapis.com/css2?family=Comfortaa:wght@400;700&family=Open+Sans:wght@400;700&display=swap" rel="stylesheet">
<style>
  :root {
    --brand: #1e96d3;
    --brand-light: #34a6d7;
    --accent: #e24c2a;
    --text: #555b60;
    --dark: #444c52;
    --panel-grey: rgba(240, 241, 242, 0.95);
    --white: #ffffff;
  }
  * { margin: 0; padding: 0; box-sizing: border-box; }
  html, body { width: 980px; height: 1200px; overflow: hidden; }
  body { position: relative; font-family: "Open Sans", sans-serif; color: var(--text); background: var(--white); }

  .site-header { position: absolute; left: 0; top: 0; width: 980px; height: 100px; background: var(--brand); }
  .brand-name { position: absolute; left: 96px; top: 24px; font-family: "Open Sans", sans-serif; font-weight: 700; font-size: 38px; color: var(--white); letter-spacing: -0.5px; }
  .main-nav { position: absolute; right: 90px; top: 42px; display: flex; gap: 15px; }
  .main-nav a { color: var(--white); text-decoration: none; font-size: 12px; }

  .hero { position: absolute; left: 0; top: 100px; width: 980px; height: 445px; }
  .hero-photo { position: absolute; inset: 0; background:
      radial-gradient(ellipse at 50% 55%, #d8c9b8 0%, transparent 35%),
      linear-gradient(100deg, #8a5a57 0%, #c9c6c3 30%, #6f6761 55%, #a9a8a6 80%, #d2d2d0 100%); }

  .finder { position: absolute; left: 619px; top: 55px; width: 271px; height: 359px; }
  .finder-search { height: 150px; background: var(--brand); padding: 30px 15px 0; }
  .finder-title { display: flex; align-items: center; gap: 12px; padding-left: 4px; }
  .finder-title h2 { font-family: "Comfortaa", sans-serif; font-weight: 400; font-size: 18px; line-height: 24px; color: var(--white); }
  .search-field { margin-top: 11px; height: 37px; background: var(--white); display: flex; align-items: center; justify-content: space-between; padding: 0 10px 0 15px; font-size: 11px; color: var(--brand); }
  .finder-info { height: 209px; background: var(--panel-grey); padding: 28px 18px 0 19px; position: relative; }
  .finder-info h3 { font-family: "Comfortaa", sans-serif; font-weight: 400; font-size: 18px; line-height: 24px; color: var(--brand); }
  .finder-info h3 strong { font-weight: 700; }
  .finder-info p { margin-top: 10px; font-size: 11.5px; line-height: 14px; color: var(--text); }
  .slide-arrow { position: absolute; top: 164px; }
  .slide-arrow.prev { left: 16px; }
  .slide-arrow.next { right: 20px; }

  .activity { position: absolute; left: 98px; top: 604px; width: 800px; }
  .activity-item { position: absolute; display: flex; align-items: center; gap: 14px; }
  .activity-item svg { flex: none; }
  .activity-text { font-size: 15.5px; line-height: 18px; color: var(--text); padding-top: 18px; }
  .handle { color: var(--brand); }
  .spot { color: var(--accent); }

  .join-band { position: absolute; left: 0; top: 987px; width: 980px; height: 161px; background: var(--brand); text-align: center; }
  .join-band p { margin-top: 34px; font-family: "Comfortaa", sans-serif; font-size: 14px; color: var(--white); }
  .join-button { display: inline-block; margin-top: 16px; width: 222px; height: 53px; line-height: 50px; background: var(--dark); color: var(--white); font-family: "Comfortaa", sans-serif; font-size: 29px; text-decoration: none; }

  .site-footer { position: absolute; left: 0; top: 1148px; width: 980px; height: 52px; background: var(--dark); }
  .footer-links { position: absolute; left: 96px; top: 18px; display: flex; gap: 12px; }
  .footer-links a { color: var(--white); text-decoration: none; font-size: 11px; }
  .powered { position: absolute; right: 112px; top: 14px; font-size: 11px; color: var(--white); display: flex; align-items: center; gap: 10px; }
  .powered strong { font-size: 16px; font-weight: 700; }
</style>
</head>
<body>
  <header class="site-header">
    <div class="brand-name">Wozzlent</div>
    <nav class="main-nav"><a href="#">SIGN UP</a><a href="#">LOGIN</a></nav>
  </header>

  <section class="hero">
    <div class="hero-photo" role="img" aria-label="Photo of a young woman with a laptop sitting on a station platform beside a high-speed train"></div>
    <div class="finder">
      <div class="finder-search">
        <div class="finder-title">
          <svg width="42" height="42" viewBox="0 0 42 42" fill="none" stroke="#fff" stroke-width="3" stroke-linejoin="round">
            <path d="M21 27 C16 20 11 16 11 11 A10 10 0 0 1 31 11 C31 16 26 20 21 27Z"/>
            <circle cx="21" cy="11" r="3.5"/>
            <path d="M4 38 L11 30 L18 36 L26 30 L32 36 L38 30 L32 38 L26 34 L18 40 L11 34 Z"/>
          </svg>
          <h2>Who would you like<br>to find?</h2>
        </div>
        <div class="search-field">
          <span>enter !wozz...</span>
          <svg width="22" height="22" viewBox="0 0 22 22" fill="none" stroke="var(--brand)" stroke-width="3" stroke-linecap="round"><circle cx="9" cy="9" r="6.5"/><path d="M14 14 L20 20"/></svg>
        </div>
      </div>
      <div class="finder-info">
        <h3>Save and manage your<br><strong>important business<br>locations.</strong></h3>
        <p>Home, work, favourite fishing or camping spot or any physical location on earth! Wozzlent is your address for life.</p>
        <svg class="slide-arrow prev" width="30" height="30" viewBox="0 0 30 30" fill="none" stroke="var(--brand)" stroke-width="2.5"><circle cx="15" cy="15" r="13"/><path d="M17 9 L11 15 L17 21"/></svg>
        <svg class="slide-arrow next" width="30" height="30" viewBox="0 0 30 30" fill="none" stroke="var(--brand)" stroke-width="2.5"><circle cx="15" cy="15" r="13"/><path d="M13 9 L19 15 L13 21"/></svg>
      </div>
    </div>
  </section>

  <section class="activity">
    <div class="activity-item" style="left:0;top:0">
      <svg width="53" height="68" viewBox="0 0 64 82" role="img" aria-label="Profile photo of mirelvo"><path d="M32 81 C26 70 2 54 2 32 A30 30 0 0 1 62 32 C62 54 38 70 32 81Z" fill="var(--brand)"/><circle cx="32" cy="32" r="25" fill="#fff"/><circle cx="32" cy="32" r="22.5" fill="#7d6a62"/></svg>
      <div class="activity-text"><span class="handle">!mirelvo</span> updated their current location<br><span class="spot">!mirelvo.now</span> 7 hours ago</div>
    </div>
    <div class="activity-item" style="left:417px;top:0">
      <svg width="53" height="68" viewBox="0 0 64 82" role="img" aria-label="Profile photo of tansoria"><path d="M32 81 C26 70 2 54 2 32 A30 30 0 0 1 62 32 C62 54 38 70 32 81Z" fill="var(--brand)"/><circle cx="32" cy="32" r="25" fill="#fff"/><circle cx="32" cy="32" r="22.5" fill="#a08672"/></svg>
      <div class="activity-text"><span class="handle">!tansoria</span> updated their current location<br><span class="spot">!tansoria.now</span> 12 hours ago</div>
    </div>
    <div class="activity-item" style="left:0;top:108px">
      <svg width="53" height="68" viewBox="0 0 64 82" role="img" aria-label="Profile photo of kelbin"><path d="M32 81 C26 70 2 54 2 32 A30 30 0 0 1 62 32 C62 54 38 70 32 81Z" fill="var(--brand)"/><circle cx="32" cy="32" r="25" fill="#fff"/><circle cx="32" cy="32" r="22.5" fill="#8f6e5c"/></svg>
      <div class="activity-text"><span class="handle">!kelbin</span> updated their current location<br><span class="spot">!kelbin.now</span> 14 hours ago</div>
    </div>
    <div class="activity-item" style="left:417px;top:108px">
      <svg width="53" height="68" viewBox="0 0 64 82" role="img" aria-label="Profile photo of jorvat88"><path d="M32 81 C26 70 2 54 2 32 A30 30 0 0 1 62 32 C62 54 38 70 32 81Z" fill="var(--brand)"/><circle cx="32" cy="32" r="25" fill="#fff"/><circle cx="32" cy="32" r="22.5" fill="#6c4a4e"/></svg>
      <div class="activity-text"><span class="handle">!jorvat88</span> added a location<br><span class="spot">!jorvat88.home</span> 15 hours ago</div>
    </div>
    <div class="activity-item" style="left:0;top:217px">
      <svg width="53" height="68" viewBox="0 0 64 82" role="img" aria-label="Profile photo of mirelvo"><path d="M32 81 C26 70 2 54 2 32 A30 30 0 0 1 62 32 C62 54 38 70 32 81Z" fill="var(--brand)"/><circle cx="32" cy="32" r="25" fill="#fff"/><circle cx="32" cy="32" r="22.5" fill="#7d6a62"/></svg>
      <div class="activity-text"><span class="handle">!mirelvo</span> updated their current location<br><span class="spot">!mirelvo.now</span> 7 hours ago</div>
    </div>
    <div class="activity-item" style="left:417px;top:217px">
      <svg width="53" height="68" viewBox="0 0 64 82" role="img" aria-label="Profile photo of tansoria"><path d="M32 81 C26 70 2 54 2 32 A30 30 0 0 1 62 32 C62 54 38 70 32 81Z" fill="var(--brand)"/><circle cx="32" cy="32" r="25" fill="#fff"/><circle cx="32" cy="32" r="22.5" fill="#a08672"/></svg>
      <div class="activity-text"><span class="handle">!tansoria</span> updated their current location<br><span class="spot">!tansoria.now</span> 12 hours ago</div>
    </div>
  </section>

  <section class="join-band">
    <p>Lorem ipsum dolor sit amet, consectetur adipisicing elit, sed do eiusmod tempor incidore magna aliqua.</p>
    <a class="join-button" href="#">join now</a>
  </section>

  <footer class="site-footer">
    <nav class="footer-links">
      <a href="#">About</a><a href="#">Help</a><a href="#">Contact</a><a href="#">Privacy</a><a href="#">Terms</a><a href="#">Refunds</a><a href="#">Faq</a>
    </nav>
    <div class="powered"><span>Powered by</span><strong>Wozzlent</strong></div>
  </footer>
</body>
</html>
```